KVL cards

Design business cards for renamed business. Korvane Lighting Limited is a leading contract designer of electronic lighting products sepcialising in LED lighting. Need a design that is simple but clear please. Cards for two persons requried.

Target Market(s)

Professional and technical

Industry/Entity Type

Business

Font styles to use
Sans Serif
Other font styles liked:
• tahoma

Colors
ffcf3e

```html
<!DOCTYPE html>
<html lang="en">
<head>
<meta charset="utf-8">
<title>Korvane Lighting Limited – Business Card</title>
<link rel="stylesheet" href="https://fonts.googleapis.com/css2?family=Noto+Sans:wght@400&display=swap">
<style>
  :root {
    --brand-yellow: #ffcf3e;
    --charcoal: #3a3d40;
    --white: #ffffff;
    --backdrop: #e6e6e4;
  }
  html, body {
    margin: 0;
    padding: 0;
    width: 1200px;
    height: 665px;
    overflow: hidden;
    background: var(--backdrop);
  }
  .stage {
    position: relative;
    width: 1200px;
    height: 665px;
  }
  .business-card {
    position: absolute;
    left: 415px;
    top: 33px;
    width: 370px;
    height: 598px;
    background: var(--brand-yellow);
    overflow: hidden;
    font-family: "Noto Sans", Tahoma, sans-serif;
    box-shadow: 0 6px 18px rgba(0, 0, 0, 0.18);
  }
  .card-shapes {
    position: absolute;
    inset: 0;
    width: 100%;
    height: 100%;
  }
  .brand-name {
    position: absolute;
    left: 40px;
    top: 44px;
    margin: 0;
    font-size: 33px;
    font-weight: 400;
    line-height: 1.2;
    color: var(--charcoal);
  }
  .brand-line {
    display: block;
    white-space: nowrap;
  }
  .person {
    position: absolute;
    left: 43px;
    top: 262px;
    color: var(--charcoal);
  }
  .person-title {
    margin: 0;
    font-size: 19px;
    line-height: 1.1;
  }
  .person-name {
    margin: 0;
    font-size: 30px;
    line-height: 1.1;
    font-weight: 400;
  }
  .contact-list {
    position: absolute;
    left: 42px;
    top: 412px;
    margin: 0;
    padding: 0;
    list-style: none;
  }
  .contact-item {
    display: flex;
    align-items: center;
    height: 30px;
    margin-bottom: 22px;
    color: var(--white);
    font-size: 21px;
  }
  .contact-icon {
    width: 30px;
    height: 30px;
    margin-right: 15px;
    flex: none;
  }
</style>
</head>
<body>
<main class="stage">
  <article class="business-card">
    <svg class="card-shapes" viewBox="0 0 343 554" preserveAspectRatio="none" aria-hidden="true">
      <path fill="var(--charcoal)" d="M343,176 C290,178 232,186 206,204 C186,220 206,244 222,258 C212,292 150,322 0,340 L0,554 L343,554 Z"/>
    </svg>

    <h1 class="brand-name">
      <span class="brand-line">Korvane Lighting</span>
      <span class="brand-line">Limited</span>
    </h1>

    <div class="person">
      <p class="person-title">CEO</p>
      <h2 class="person-name">Your name</h2>
    </div>

    <ul class="contact-list">
      <li class="contact-item">
        <svg class="contact-icon" viewBox="0 0 30 30" aria-hidden="true">
          <circle cx="15" cy="15" r="13" fill="none" stroke="var(--brand-yellow)" stroke-width="2"/>
          <path fill="var(--brand-yellow)" d="M10.5,8.5 l2.5,-0.5 l1.5,3.5 l-1.8,1.3 c0.8,1.8 2.2,3.2 4,4 l1.3,-1.8 l3.5,1.5 l-0.5,2.5 c-0.3,1 -1.3,1.5 -2.3,1.3 c-4.5,-1 -8,-4.5 -9,-9 c-0.2,-1 0.3,-2 1.3,-2.3 z"/>
        </svg>
        <span>0777 777 777</span>
      </li>
      <li class="contact-item">
        <svg class="contact-icon" viewBox="0 0 30 30" aria-hidden="true">
          <circle cx="15" cy="15" r="13" fill="none" stroke="var(--brand-yellow)" stroke-width="2"/>
          <path fill="none" stroke="var(--brand-yellow)" stroke-width="1.4" d="M7,15 l1.5,-2 l1.5,2 l1.5,-2 l1.5,2 l1.5,-2 l1.5,2 l1.5,-2 l1.5,2 l1.5,-2 l1.5,2"/>
        </svg>
        <span>website.com</span>
      </li>
      <li class="contact-item">
        <svg class="contact-icon" viewBox="0 0 30 30" aria-hidden="true">
          <circle cx="15" cy="15" r="13" fill="none" stroke="var(--brand-yellow)" stroke-width="2"/>
          <text x="15" y="20.5" text-anchor="middle" font-family="Noto Sans, sans-serif" font-size="16" fill="var(--brand-yellow)">@</text>
        </svg>
        <span>your@email.com</span>
      </li>
    </ul>
  </article>
</main>
</body>
</html>
```